Poster Design

Hello,

My name is Rowan Tilbury and I run a youtube channel called 'DriftingNotes'. I want a poster made for those who watch my video to purchase and put on their wall at home. The poster will be all text and as you can see, I've attached a few examples of posters which I would like it to be similar to. I use a lot of the colour #ab6f7f so it would be good to incorporate this in somewhere (maybe the background colour).
I would like the poster to say:
"Do More Of What Makes YOU Happy"
I need this poster to be for sale ready for christmas, so Im going to need the designs created as soon as possible. Im sorry for the rush.
Have fun with it and feel free to upload multiple versions of a design as well as a few designs if you like.
I look forward to seeing what you come up with.
Rowan
(Of course I will need to own all rights once the payment has been made)

```html
<!DOCTYPE html>
<html lang="en">
<head>
<meta charset="utf-8">
<title>Do More Of What Makes You Happy – Poster</title>
<link rel="stylesheet" href="https://fonts.googleapis.com/css2?family=Lobster+Two:ital,wght@1,700&family=Oswald:wght@600&family=Quicksand:wght@300&display=swap">
<style>
  :root {
    --poster-mauve: #ab6f7f;
    --poster-mauve-deep: #91566a;
    --cream: #f3ecdf;
    --plum: #5b3142;
    --plum-dark: #4a2736;
    --shadow: rgba(74, 36, 52, 0.75);
  }
  * { margin: 0; padding: 0; box-sizing: border-box; }
  html, body {
    width: 873px;
    height: 1200px;
    overflow: hidden;
    background: var(--poster-mauve);
  }
  .poster {
    position: relative;
    width: 873px;
    height: 1200px;
    background: radial-gradient(ellipse at 50% 42%, #b07585 0%, var(--poster-mauve) 45%, var(--poster-mauve-deep) 100%);
    overflow: hidden;
  }
  .poster__frame {
    position: absolute;
    inset: 20px;
    border: 4px solid var(--cream);
  }
  .line {
    position: absolute;
    left: 0;
    width: 100%;
    text-align: center;
    color: var(--cream);
    white-space: nowrap;
    text-shadow: 5px 6px 0 var(--shadow);
  }
  .line--script {
    font-family: "Lobster Two", cursive;
    font-style: italic;
    font-weight: 700;
  }
  .line--block {
    font-family: "Oswald", sans-serif;
    font-weight: 600;
    letter-spacing: 2px;
  }
  .line--do { top: 166px; font-size: 120px; line-height: 1; }
  .line--more { top: 256px; font-size: 175px; line-height: 1.1; }
  .line--of-what { top: 440px; font-size: 130px; line-height: 1; }
  .line--you { top: 700px; font-size: 176px; line-height: 1.1; }
  .line--happy { top: 852px; font-size: 160px; line-height: 1; }

  .ribbon {
    position: absolute;
    left: 0;
    top: 590px;
    width: 873px;
    height: 135px;
  }
  .ribbon__tail { fill: var(--plum); }
  .ribbon__fold { fill: var(--plum-dark); }
  .ribbon__band { fill: var(--plum); }
  .ribbon__word {
    position: absolute;
    left: 0;
    top: 598px;
    width: 100%;
    text-align: center;
    font-family: "Quicksand", sans-serif;
    font-weight: 300;
    font-size: 86px;
    line-height: 1;
    color: var(--cream);
    letter-spacing: 3px;
  }
  .rays {
    position: absolute;
    left: 0;
    top: 745px;
    width: 873px;
    height: 100px;
  }
  .rays line {
    stroke: var(--cream);
    stroke-width: 6;
    stroke-linecap: round;
  }
</style>
</head>
<body>
  <main class="poster">
    <div class="poster__frame"></div>

    <p class="line line--script line--do">Do</p>
    <p class="line line--block line--more">MORE</p>

    <svg class="ribbon" viewBox="0 0 873 135" aria-hidden="true">
      <polygon class="ribbon__tail" points="250,42 136,42 176,87 136,132 268,132 268,42"/>
      <polygon class="ribbon__tail" points="623,42 737,42 697,87 737,132 605,132 605,42"/>
      <polygon class="ribbon__fold" points="250,110 268,132 268,110"/>
      <polygon class="ribbon__fold" points="623,110 605,132 605,110"/>
      <rect class="ribbon__band" x="250" y="0" width="373" height="110"/>
    </svg>
    <p class="ribbon__word">makes</p>

    <p class="line line--script line--of-what">of what</p>

    <svg class="rays" viewBox="0 0 873 100" aria-hidden="true">
      <line x1="204" y1="18" x2="280" y2="36"/>
      <line x1="192" y1="54" x2="282" y2="52"/>
      <line x1="204" y1="90" x2="280" y2="70"/>
      <line x1="669" y1="18" x2="593" y2="36"/>
      <line x1="681" y1="54" x2="591" y2="52"/>
      <line x1="669" y1="90" x2="593" y2="70"/>
    </svg>

    <p class="line line--block line--you">YOU</p>
    <p class="line line--script line--happy">happy</p>
  </main>
</body>
</html>
```